Looking for a website that shows the services available to customers.This company will provide consulting on how to reduce costs and improve overal IT spend within any organization. We will employ experts in many aspects of IT including Cloud, Mainframe, KV720/eStrand/TVault, Disaster Recovery, IT optimization strategies, Colocation, Hybrid IT, Migrations, Networking, Security etc. I am a technology advisor that helps to optimize costs in IT

Target Market(s)

Al companies over $1M in revenue

Industry/Entity Type

It Company

Number of Pages Required

5+ page

Font styles to use
Serif
Sans Serif

Requirements
Must have
• Tabs for: About us (our team), Services, Why Vanmoor, Testimonials, Contact Us
Nice to have
• i would like to have on my services pages some logos of partners. Such as dravolex, ZN&P, etc.

I need an understanding of how to add/change to the website
Should not have
• no spirlay fonts or any thing scrolly. I want t professional IT website

```html
<!DOCTYPE html>
<html lang="en">
<head>
<meta charset="utf-8">
<title>Vanmoor – A Clear Path to IT Optimization</title>
<link rel="stylesheet" href="https://fonts.googleapis.com/css2?family=Catamaran:wght@600;700;800&family=Lato:ital,wght@0,400;0,700;1,400&display=swap">
<style>
:root{
  --blue:#1b72bd;
  --green:#78b83a;
  --teal:#2aa79d;
  --ink:#1c1c1c;
  --text:#333;
  --grey-band:#f2f2f3;
  --grey-soft:#f5f5f6;
  --footer:#232323;
  --footer-bar:#1b1b1b;
  --white:#fff;
}
*{box-sizing:border-box;margin:0;padding:0}
html,body{width:1200px;height:3341px;overflow:hidden}
body{position:relative;background:var(--white);font-family:"Lato",sans-serif;color:var(--text)}
.abs{position:absolute}
h1,h2,h3,.brand{font-family:"Catamaran",sans-serif}

/* header */
.site-header{left:0;top:0;width:1200px;height:123px;background:var(--white)}
.brand{display:flex;align-items:center;gap:10px;font-weight:700;color:var(--ink)}
.brand-dot{width:16px;height:16px;border-radius:50%;background:var(--blue)}
.site-header .brand{left:75px;top:46px;font-size:40px}
.main-nav a{position:absolute;top:66px;font-weight:700;font-size:16px;color:var(--ink);text-decoration:none}
.main-nav a.active{color:var(--blue)}

/* hero */
.hero{left:0;top:123px;width:1200px;height:588px;background:linear-gradient(100deg,#1a2d4a 0%,#27507a 40%,#3b6a93 65%,#2a3d58 100%)}
.hero h1{left:75px;top:165px;font-size:96px;line-height:1;font-weight:800;color:var(--white)}
.hero .tagline{left:77px;top:272px;font-family:"Catamaran",sans-serif;font-size:44px;font-weight:700;color:var(--white)}
.btn{display:flex;align-items:center;gap:14px;font-weight:700;font-size:18px;color:var(--white);background:var(--green);padding:0 20px;height:56px}
.hero .btn{left:75px;top:353px;width:165px}
.arrow-circle{width:16px;height:16px}

/* partners */
.partners{left:0;top:711px;width:1200px;height:142px;background:var(--grey-band)}
.partners .label{left:75px;top:62px;font-weight:700;font-size:16px;color:var(--ink)}
.partner{display:flex;align-items:center;gap:8px;font-family:"Lato",sans-serif;font-weight:700;font-size:28px;color:#555;top:48px}
.partner-mark{width:26px;height:26px;background:#8a8a8a}

/* welcome */
.welcome-art{left:78px;top:908px;width:584px;height:441px;background:radial-gradient(circle at 55% 55%,#e6eef8 0%,#f1f5fb 55%,#fff 80%)}
.section-title{font-weight:700;color:var(--ink);font-size:40px;line-height:1}
.welcome h2{left:663px;top:998px}
.body-copy{font-size:16.5px;line-height:34px;color:var(--text)}
.welcome .body-copy{left:616px;top:1054px;width:500px}
.link-more{display:flex;align-items:center;gap:14px;font-weight:700;font-size:18px;color:var(--blue)}
.welcome .link-more{left:614px;top:1284px}

/* solutions */
.solutions-bg{left:0;top:1390px;width:1200px;height:460px}
.solutions h2{left:122px;top:1512px}
.solutions .body-copy{left:76px;top:1574px;width:310px;line-height:26px;font-size:16.5px;color:var(--ink)}
.pager{display:flex;gap:14px}
.solutions .pager{left:76px;top:1726px}
.card{background:var(--white);box-shadow:0 2px 10px rgba(0,0,0,.16);width:214px;height:233px;top:1518px;padding:18px 16px}
.card svg{display:block;width:72px;height:72px}
.card h3{font-size:23px;font-weight:700;color:var(--blue);margin-top:8px;line-height:1.2}
.card p{font-size:14.5px;line-height:24px;color:var(--ink);margin-top:4px}

/* why */
.why-photo{left:0;top:1856px;width:586px;height:546px;background:linear-gradient(90deg,#2d3236 0%,#6b7275 45%,#c9cdd0 75%,#e4e6e7 100%)}
.why-panel{left:419px;top:1917px;width:781px;height:424px;background:linear-gradient(180deg,var(--teal) 0%,#28a39b 100%)}
.why-panel h2{left:99px;top:86px;color:var(--white);font-size:40px}
.why-panel .body-copy{left:52px;top:142px;width:690px;color:var(--white);line-height:37px;font-size:16.5px}
.why-panel .link-more{left:50px;top:315px;color:var(--white)}

/* testimonials */
.testi-bg{left:0;top:2440px;width:1200px;height:527px}
.testi-side{left:0;top:2610px;width:237px;height:280px;background:linear-gradient(180deg,#e8e8e8,#cfcfcf);box-shadow:0 2px 8px rgba(0,0,0,.15)}
.testi-card{left:266px;top:2610px;width:512px;height:280px;background:linear-gradient(135deg,var(--teal) 0%,#2a8fb4 100%);box-shadow:0 2px 8px rgba(0,0,0,.15)}
.testi-card .quote{left:29px;top:48px;width:290px;font-style:italic;font-size:15.5px;line-height:30px;color:var(--white)}
.testi-card .name{left:29px;top:180px;font-weight:700;font-size:17px;color:var(--white)}
.testi-card .role{left:29px;top:208px;font-style:italic;font-size:14px;color:#d8f2f0}
.testi-card .portrait{left:305px;top:0;width:207px;height:280px;background:linear-gradient(180deg,#3a8fb0 0%,#23314a 100%)}
.testimonials h2{right:73px;top:2636px}
.testimonials .body-copy{right:73px;top:2696px;width:330px;text-align:right;line-height:26px;color:var(--ink)}
.testimonials .pager{right:73px;top:2848px}

/* footer */
.site-footer{left:0;top:2967px;width:1200px;height:309px;background:var(--footer);color:#e6e6e6}
.site-footer .brand{left:75px;top:95px;font-size:40px;color:var(--white)}
.social{left:75px;top:189px;display:flex;gap:15px}
.social span{width:34px;height:34px;border:1.5px solid #bbb;border-radius:50%}
.footer-col h3{position:absolute;font-size:20px;font-weight:700;color:var(--white);top:58px}
.footer-col a{position:absolute;font-size:14.5px;color:#e6e6e6;text-decoration:none;white-space:nowrap}
.footer-bar{left:0;top:3276px;width:1200px;height:65px;background:var(--footer-bar);text-align:center;padding-top:22px;font-size:12.5px;color:#9a9a9a}
</style>
</head>
<body>

<header class="abs site-header">
  <div class="abs brand"><span class="brand-dot"></span>Vanmoor</div>
  <nav class="main-nav">
    <a class="active" style="left:460px" href="#">Home</a>
    <a style="left:547px" href="#">About Us</a>
    <a style="left:660px" href="#">Services</a>
    <a style="left:765px" href="#">Why Vanmoor</a>
    <a style="left:904px" href="#">Testimonials</a>
    <a style="left:1041px" href="#">Contact Us</a>
  </nav>
</header>

<section class="abs hero" role="img" aria-label="Photo of two engineers with a laptop in a server room">
  <h1 class="abs">Vanmoor</h1>
  <p class="abs tagline">A Clear Path to IT Optimization</p>
  <a class="abs btn">Read More
    <svg class="arrow-circle" viewBox="0 0 16 16"><circle cx="8" cy="8" r="8" fill="#fff"/><path d="M6.5 4.5 10 8l-3.5 3.5" stroke="#78b83a" stroke-width="2" fill="none"/></svg>
  </a>
</section>

<section class="abs partners">
  <p class="abs label">OUR PARTNERS:</p>
  <div class="abs partner" style="left:281px"><span class="partner-mark"></span>dravolex</div>
  <div class="abs partner" style="left:493px">ZN&amp;P</div>
  <div class="abs partner" style="left:698px">Nimbara</div>
  <div class="abs partner" style="left:902px">Trellon</div>
</section>

<section class="welcome">
  <div class="abs welcome-art" role="img" aria-label="Illustration of people working with cloud services, devices and charts"></div>
  <h2 class="abs section-title">Welcome to Vanmoor</h2>
  <div class="abs body-copy">
    <p>In a complex world of IT.Vanmoor will assist you in optimizing IT spend.&nbsp; Our 20 plus years in the IT industry brings best of breed personnel from Data center, Managed Services, and Disaster Recovery, to help you get the best solutions for the best price.</p>
    <p style="margin-top:14px">In a complex world of IT, let us help simplify.</p>
  </div>
  <a class="abs link-more">Read More
    <svg class="arrow-circle" viewBox="0 0 16 16"><circle cx="8" cy="8" r="8" fill="#1b72bd"/><path d="M6.5 4.5 10 8l-3.5 3.5" stroke="#fff" stroke-width="2" fill="none"/></svg>
  </a>
</section>

<section class="solutions">
  <svg class="abs solutions-bg" viewBox="0 0 1200 460" preserveAspectRatio="none"><path d="M0 120 C300 140 520 100 700 40 C850 -10 1000 0 1200 30 L1200 460 L0 460 Z" fill="#f5f5f6"/></svg>
  <h2 class="abs section-title">Our Solutions</h2>
  <p class="abs body-copy">Neque porro quisquam est qui dolorem ipsum quia dolor sit amet, aecenas iaculis sem ut enim semper elementum. Vestibulum mi erat, sodales vel est a.</p>
  <div class="abs pager">
    <svg width="14" height="20" viewBox="0 0 14 20"><path d="M11 2 3 10l8 8" stroke="#1b72bd" stroke-width="3" fill="none"/></svg>
    <svg width="14" height="20" viewBox="0 0 14 20"><path d="M3 2l8 8-8 8" stroke="#1b72bd" stroke-width="3" fill="none"/></svg>
  </div>
  <article class="abs card" style="left:432px">
    <svg viewBox="0 0 72 72" fill="none" stroke="#6aa93a" stroke-width="2.5"><path d="M16 44h40a10 10 0 0 0 0-20 14 14 0 0 0-27-4A11 11 0 0 0 16 44z"/><circle cx="26" cy="56" r="6"/><rect x="42" y="48" width="20" height="16"/></svg>
    <h3>Cloud</h3>
    <p>In todays quickly changing IT environment companies have a lot of choices.</p>
  </article>
  <article class="abs card" style="left:672px">
    <svg viewBox="0 0 72 72" fill="none" stroke="#6aa93a" stroke-width="2.5"><rect x="22" y="6" width="40" height="12"/><rect x="22" y="22" width="40" height="12"/><rect x="22" y="38" width="40" height="12"/><path d="M6 62h22l14-8"/></svg>
    <h3>Data Center</h3>
    <p>Todays data centers are complex and have many moving parts.</p>
  </article>
  <article class="abs card" style="left:912px">
    <svg viewBox="0 0 72 72" fill="none" stroke="#6aa93a" stroke-width="2.5"><circle cx="36" cy="34" r="12"/><circle cx="10" cy="12" r="6"/><circle cx="62" cy="12" r="6"/><path d="M22 70V58a14 14 0 0 1 28 0v12"/></svg>
    <h3>Managed Services</h3>
    <p>In todays quickly changing IT environment companies have a lot of choices.</p>
  </article>
</section>

<section class="why">
  <div class="abs why-photo" role="img" aria-label="Photo of two colleagues reviewing a laptop beside server racks"></div>
  <div class="abs why-panel">
    <h2 class="abs section-title">Why Vanmoor ?</h2>
    <p class="abs body-copy">Lorem ipsum dolor sit amet, consectetur adipiscing elit. Integer luctus malesuada fringilla. Nullam dignissim, elit sed pellentesque accumsan, nibh dui dictum enim, eget pulvinar justo tellus non nunc. Vestibulum gravida quam ipsum, ut volutpat ipsum tempor vel. Donec ut urna ut orci congue suscipit quis ut lectus.</p>
    <a class="abs link-more">Read More
      <svg class="arrow-circle" viewBox="0 0 16 16"><circle cx="8" cy="8" r="8" fill="#fff"/><path d="M6.5 4.5 10 8l-3.5 3.5" stroke="#2aa79d" stroke-width="2" fill="none"/></svg>
    </a>
  </div>
</section>

<section class="testimonials">
  <svg class="abs testi-bg" viewBox="0 0 1200 527" preserveAspectRatio="none"><path d="M0 100 C250 20 450 0 650 60 C850 120 1000 110 1200 70 L1200 527 L0 527 Z" fill="#f5f5f6"/></svg>
  <div class="abs testi-side" role="img" aria-label="Portrait of a client"></div>
  <div class="abs testi-card">
    <p class="abs quote">“ Neque porro quisquam est qui dolorem ipsum quia dolor sit amet, aecenas iaculis sem ut enim semper elementum mi erat, sodales vel est sem ut enim semper..”</p>
    <p class="abs name">Name Heading</p>
    <p class="abs role">Eget pulvinar justo tellus non nunc</p>
    <div class="abs portrait" role="img" aria-label="Portrait of a client in a suit"></div>
  </div>
  <h2 class="abs section-title">Testimonials</h2>
  <p class="abs body-copy">Neque porro quisquam est qui dolorem ipsum quia dolor sit amet, aecenas iaculis sem ut enim semper elementum. Vestibulum mi erat, sodales vel est a.</p>
  <div class="abs pager">
    <svg width="14" height="20" viewBox="0 0 14 20"><path d="M11 2 3 10l8 8" stroke="#1b72bd" stroke-width="3" fill="none"/></svg>
    <svg width="14" height="20" viewBox="0 0 14 20"><path d="M3 2l8 8-8 8" stroke="#1b72bd" stroke-width="3" fill="none"/></svg>
  </div>
</section>

<footer class="abs site-footer">
  <div class="abs brand"><span class="brand-dot"></span>Vanmoor</div>
  <div class="abs social" aria-label="Social links"><span></span><span></span><span></span><span></span><span></span></div>
  <div class="footer-col">
    <h3 style="left:355px">Site Map</h3>
    <a style="left:355px;top:102px">Home</a>
    <a style="left:355px;top:139px">About us</a>
    <a style="left:355px;top:176px">Services</a>
    <a style="left:455px;top:102px">Why Vanmoor</a>
    <a style="left:455px;top:139px">Testimonials</a>
    <a style="left:455px;top:176px">Contact Us</a>
  </div>
  <div class="footer-col">
    <h3 style="left:612px">Services</h3>
    <a style="left:612px;top:102px">Neque porro</a>
    <a style="left:612px;top:139px">Quisquam est qui</a>
    <a style="left:612px;top:176px">Dolorem ipsum quia</a>
    <a style="left:612px;top:213px">Dolor sit amet</a>
    <a style="left:612px;top:250px">Consectetur</a>
  </div>
  <div class="footer-col">
    <h3 style="left:820px">Solutions</h3>
    <a style="left:820px;top:102px">Cloud</a>
    <a style="left:820px;top:139px">Mainframe</a>
    <a style="left:820px;top:176px">KV720/eStrand/TVault</a>
    <a style="left:820px;top:213px">Disaster Recovery</a>
    <a style="left:820px;top:250px">IT Optimization Strategies</a>
    <a style="left:1031px;top:102px">Colocation</a>
    <a style="left:1031px;top:139px">Hybrid IT</a>
    <a style="left:1031px;top:176px">Migrations</a>
    <a style="left:1031px;top:213px">Networking</a>
    <a style="left:1031px;top:250px">Security</a>
  </div>
</footer>
<div class="abs footer-bar">Copyright © 2020 Company Name&nbsp; All rights reserved</div>

</body>
</html>
```